App UI Design: Shopping/E-commerce App

Project :
Develop an UI design & App icon for an E-commerce/Shopping App

About the App/ Target Audience:
This grocery & food shopping app will be used by independent pub, café, restaurant owners to place & manage their purchases of foods and groceries for their catering businesses.

They will use the app to access product catalogues & special promotions, search & buy large quantities of groceries or catering supplies, and the ability to manage and track status of their order.

The HTML5 App’s has been built with a very basic structure. It now needs the visual layer of the UI designed

Note:
The app is tailored for business & catering orders, not retail/supermarket buyers, so the visual needs to look smart & not too casual.

Reason: Current submissions have not met out expectations. Please use the similar app examples in the PDF as a strong point of reference for the look & feel. Feedback will be given as submissions come in, please feel free to submit initial concepts of 1 or 2 of the pages & we'll provide feedback on whether it is on the right track or not before you do more work. Current submission will also receive feedback in the next few days. We look forward to new submissions!

Target Market(s)

Male & Female. Independent pub, café, restaurant owners buying for their catering businesses. Chefs etc.

Industry/Entity Type

Restaurant

Requirements
Must have
• An overview of elements/pages of the app that needs to be designed are:
(DOWNLOAD a more detailed diagram PDF explanation)

1. Welcome- Log-in Page
2. Homepage – index that links to different function of the app

Products:
3. Promotions page – for products on special for a limited time
4. Catalogue page – access to a range of catalogue

Ways to buy:
5. Basket (Shopping Cart) - tracking items they are buying from the catalogues
6. Templates (Pre-set Shopping list)- Set shopping list that has been preloaded for certain menu
7. Open Order page

My Account:
8. My Account/profile page – Users can check the status of their order, look at past orders, look at their account number & details etc

_______________________________________________________

Icon set- Icons to represent each pages that act as visual cues for easier browsing.

2 Main features that need to be accessible & consistent throughout all pages are:
a) The Navigation Bar –
so the user can quickly find their way back & access to the main functions
b) The Search bar –
whether it drops down when needed, or is featured as a header/footer.
c) Log out button
Nice to have
• _______________________________________________________

Things to keep in mind:

The UI design essentially needs to be a customizable template that can easily adapt to any brand/logo with a slight change of the color scheme. As we will later implement our brand & logo onto it.

We’re looking for a clean & clear design that allows for a straight forward easy user experience.

You are free to develop different layout & UI pattern that you feel is the most efficient way the user can walk through the App & make their purchase in no more than 2 or 3 clicks
________________________________________________

Screenshot of Similar Apps for reference are also in the PDF

```html
<!DOCTYPE html>
<html lang="en">
<head>
<meta charset="utf-8">
<title>Pantry Supply – App Screens</title>
<link href="https://fonts.googleapis.com/css2?family=Arimo:wght@400;700&display=swap" rel="stylesheet">
<style>
:root{
  --page-bg:#ececec;
  --status-bg:#000;
  --blue-light:#4a7fcc;
  --blue-mid:#3464ad;
  --blue-dark:#1d4585;
  --nav-top:#5b8fd6;
  --nav-bottom:#2d5fa8;
  --yellow:#f7c21b;
  --yellow-dark:#eea400;
  --cell-top:#f6f6f6;
  --cell-bottom:#dedede;
  --cell-line:#c9c9c9;
  --ink:#333;
  --ink-soft:#666;
  --green:#3aa62a;
  --summary:#a9a9a9;
  --white:#fff;
  --row-bg:#f3f3f3;
  --thumb:#8a5a3c;
}
*{box-sizing:border-box;margin:0;padding:0}
html,body{width:1200px;height:874px;overflow:hidden}
body{background:var(--page-bg);font-family:"Arimo",Arial,sans-serif;color:var(--ink);position:relative}

.screen{position:absolute;top:180px;width:294px;height:460px;overflow:hidden;background:var(--white);box-shadow:0 2px 8px rgba(0,0,0,.15)}
.screen--login{left:90px}
.screen--home{left:449px}
.screen--cart{left:812px}

.status-bar{height:20px;background:var(--status-bg);color:var(--white);font-size:10px;font-weight:700;display:flex;align-items:center;justify-content:space-between;padding:0 5px}
.status-bar__carrier{display:flex;align-items:center;gap:3px}
.status-bar__battery{display:flex;align-items:center;gap:3px}

.nav-bar{height:38px;background:linear-gradient(var(--nav-top),var(--nav-bottom));display:flex;align-items:center;justify-content:space-between;padding:0 14px 0 18px;border-bottom:1px solid var(--blue-dark)}
.nav-btn{font-size:7px;color:var(--white);background:linear-gradient(#6c9de0,#3a6db6);border:1px solid #2a5596;border-radius:4px;padding:2px 8px}
.nav-btn--back{clip-path:polygon(10% 0,100% 0,100% 100%,10% 100%,0 50%);padding-left:11px}
.nav-btn--logout{clip-path:polygon(0 0,90% 0,100% 50%,90% 100%,0 100%);padding-right:11px}

.brand{text-align:center;color:var(--yellow);font-weight:700;line-height:1}
.brand__name{font-size:24px;letter-spacing:-.3px}
.intro{color:var(--white);font-size:6.4px;font-weight:700;text-align:center;line-height:1.3;width:220px;margin:0 auto}

/* login */
.login{height:440px;background:radial-gradient(ellipse at 50% 45%,var(--blue-light),var(--blue-mid) 55%,var(--blue-dark));padding-top:62px}
.login .intro{margin-top:16px}
.field{display:block;width:174px;height:16px;margin:0 auto;border-radius:4px;background:var(--white);font-size:7.5px;color:var(--ink-soft);text-align:center;line-height:16px}
.field--user{margin-top:24px}
.field--pass{margin-top:14px}
.sign-in{display:block;width:85px;height:19px;margin:20px auto 0;border-radius:4px;background:linear-gradient(var(--yellow),var(--yellow-dark));color:var(--white);font-size:9px;font-weight:700;text-align:center;line-height:19px}

/* home */
.hero{height:146px;background:radial-gradient(ellipse at 50% 50%,var(--blue-light),var(--blue-mid) 60%,var(--blue-dark));padding-top:30px}
.hero .intro{margin-top:12px}
.menu-grid{display:grid;grid-template-columns:1fr 1fr}
.menu-item{height:49px;background:linear-gradient(var(--cell-top),var(--cell-bottom));border-bottom:1px solid var(--cell-line);display:flex;flex-direction:column;align-items:center;justify-content:flex-end;padding-bottom:5px;gap:6px;font-size:10.5px;color:var(--ink)}
.menu-item:nth-child(odd){border-right:1px solid var(--cell-line)}
.menu-item svg{width:13px;height:13px}
.search-strip{height:28px;background:linear-gradient(var(--white),#ececec);display:flex;align-items:center;justify-content:center;border-bottom:1px solid #ddd}
.search-box{width:126px;height:11px;border-radius:6px;background:var(--white);border:1px solid #cfcfcf;box-shadow:inset 0 1px 2px rgba(0,0,0,.15);display:flex;align-items:center;justify-content:flex-end;padding-right:10px;gap:3px;font-size:6px;color:#999}
.home-fill{height:100%;background:#f2f2f2}

/* cart */
.product-list{list-style:none}
.product{height:48px;background:linear-gradient(var(--white),var(--row-bg));border-bottom:1px solid #d3d3d3;display:flex;align-items:center;padding:0 12px 0 18px;position:relative}
.product__thumb{width:38px;height:36px;border:1px solid #cfcfcf;background:var(--white);padding:4px}
.product__thumb span{display:block;width:100%;height:100%;background:linear-gradient(#5a2e1f,var(--thumb) 60%,#d8b690)}
.product__name{margin-left:12px;font-size:9.5px;line-height:1.35;width:98px;color:var(--ink)}
.product__price{font-size:5.5px;color:var(--ink-soft);line-height:1.4}
.product__price strong{font-size:12px;color:var(--green);margin-left:3px}
.product__case{display:block;font-size:4.8px}
.product__case em{font-style:normal;color:var(--green)}
.product__actions{position:absolute;right:12px;top:6px;display:flex;flex-direction:column;align-items:center;gap:7px}
.summary{height:74px;background:var(--summary);display:flex;align-items:center;justify-content:space-between;padding:0 24px 0 34px;color:var(--white)}
.summary__count{font-size:9px;margin-top:-8px}
.summary__total{font-size:13px;margin-top:12px}
</style>
</head>
<body>

<section class="screen screen--login">
  <div class="status-bar">
    <span class="status-bar__carrier">
      <svg width="14" height="8" viewBox="0 0 14 8"><rect x="0" y="6" width="2" height="2" fill="#fff"/><rect x="3" y="4.5" width="2" height="3.5" fill="#fff"/><rect x="6" y="3" width="2" height="5" fill="#fff"/><rect x="9" y="1.5" width="2" height="6.5" fill="#fff"/><rect x="12" y="0" width="2" height="8" fill="#fff"/></svg>
      Nimbus
      <svg width="11" height="8" viewBox="0 0 11 8"><path d="M1 3a6.5 6.5 0 0 1 9 0M2.7 4.8a4 4 0 0 1 5.6 0" stroke="#fff" stroke-width="1.3" fill="none"/><circle cx="5.5" cy="7" r="1" fill="#fff"/></svg>
    </span>
    <span>4:00 PM</span>
    <span class="status-bar__battery">100% <svg width="17" height="8" viewBox="0 0 17 8"><rect x=".5" y=".5" width="14" height="7" rx="1" stroke="#fff" fill="none"/><rect x="2" y="2" width="11" height="4" fill="#fff"/><rect x="15" y="2.5" width="1.5" height="3" fill="#fff"/></svg></span>
  </div>
  <div class="login">
    <div class="brand"><span class="brand__name">Pantry Supply</span></div>
    <p class="intro">Lorem ipsum dolor sit amet, in cum iusto sonet nihil. Vel et laudem fierent. Per te duis omnes iuvaret, in nec debet splendide adversarium. Mei ad prompta necessitatibus.</p>
    <span class="field field--user">Username</span>
    <span class="field field--pass">Password</span>
    <span class="sign-in">SIGN IN</span>
  </div>
</section>

<section class="screen screen--home">
  <div class="status-bar">
    <span class="status-bar__carrier">
      <svg width="14" height="8" viewBox="0 0 14 8"><rect x="0" y="6" width="2" height="2" fill="#fff"/><rect x="3" y="4.5" width="2" height="3.5" fill="#fff"/><rect x="6" y="3" width="2" height="5" fill="#fff"/><rect x="9" y="1.5" width="2" height="6.5" fill="#fff"/><rect x="12" y="0" width="2" height="8" fill="#fff"/></svg>
      Nimbus
      <svg width="11" height="8" viewBox="0 0 11 8"><path d="M1 3a6.5 6.5 0 0 1 9 0M2.7 4.8a4 4 0 0 1 5.6 0" stroke="#fff" stroke-width="1.3" fill="none"/><circle cx="5.5" cy="7" r="1" fill="#fff"/></svg>
    </span>
    <span>4:00 PM</span>
    <span class="status-bar__battery">100% <svg width="17" height="8" viewBox="0 0 17 8"><rect x=".5" y=".5" width="14" height="7" rx="1" stroke="#fff" fill="none"/><rect x="2" y="2" width="11" height="4" fill="#fff"/><rect x="15" y="2.5" width="1.5" height="3" fill="#fff"/></svg></span>
  </div>
  <div class="nav-bar"><span class="nav-btn nav-btn--back">Back</span><span class="nav-btn nav-btn--logout">Log Out</span></div>
  <div class="hero">
    <div class="brand"><span class="brand__name">Pantry Supply</span></div>
    <p class="intro">Lorem ipsum dolor sit amet, in cum iusto sonet nihil. Vel et laudem fierent. Per te duis omnes iuvaret, in nec debet splendide adversarium. Mei ad prompta necessitatibus.</p>
  </div>
  <nav class="menu-grid">
    <div class="menu-item"><svg viewBox="0 0 13 13" fill="none" stroke="#333" stroke-width="1.2"><path d="M2 1h9M2 12h9M3 1c0 4 7 4 7 5.5S3 8 3 12M10 1c0 4-7 4-7 5.5S10 8 10 12"/></svg>PROMOTIONS</div>
    <div class="menu-item"><svg viewBox="0 0 13 13" fill="none" stroke="#333" stroke-width="1.2"><rect x="1" y="2" width="11" height="10" rx="1.5"/><path d="M1 5h11M4 1v2M9 1v2M4 8h5M4 10h3"/></svg>CATALOGUE</div>
    <div class="menu-item"><svg viewBox="0 0 13 13" fill="none" stroke="#333" stroke-width="1.2"><path d="M1 2h2l2 6h6l1-4H4"/><circle cx="5.5" cy="10.5" r="1"/><circle cx="10" cy="10.5" r="1"/></svg>BASKET</div>
    <div class="menu-item"><svg viewBox="0 0 13 13" fill="none" stroke="#333" stroke-width="1.2"><rect x="1.5" y="4" width="7" height="8" rx="1"/><path d="M4 4V1.5h7.5V9H8.5"/></svg>ORDER TEMPLATE</div>
    <div class="menu-item"><svg viewBox="0 0 13 13" fill="none" stroke="#333" stroke-width="1.2"><rect x="2" y="1" width="9" height="11" rx="1"/><path d="M4 4h5M4 6.5h5M4 9h3"/></svg>OPEN ORDER</div>
    <div class="menu-item"><svg viewBox="0 0 13 13" fill="none" stroke="#333" stroke-width="1.2"><circle cx="6.5" cy="6.5" r="2"/><path d="M6.5 1v2M6.5 10v2M1 6.5h2M10 6.5h2M2.6 2.6l1.4 1.4M9 9l1.4 1.4M2.6 10.4 4 9M9 4l1.4-1.4"/></svg>MY ACCOUNT</div>
  </nav>
  <div class="search-strip"><span class="search-box"><svg width="6" height="6" viewBox="0 0 6 6"><circle cx="3.5" cy="2.5" r="1.8" stroke="#777" fill="none"/><path d="M2.2 3.8.5 5.5" stroke="#777"/></svg>search</span></div>
  <div class="home-fill"></div>
</section>

<section class="screen screen--cart">
  <div class="status-bar">
    <span class="status-bar__carrier">
      <svg width="14" height="8" viewBox="0 0 14 8"><rect x="0" y="6" width="2" height="2" fill="#fff"/><rect x="3" y="4.5" width="2" height="3.5" fill="#fff"/><rect x="6" y="3" width="2" height="5" fill="#fff"/><rect x="9" y="1.5" width="2" height="6.5" fill="#fff"/><rect x="12" y="0" width="2" height="8" fill="#fff"/></svg>
      Nimbus
      <svg width="11" height="8" viewBox="0 0 11 8"><path d="M1 3a6.5 6.5 0 0 1 9 0M2.7 4.8a4 4 0 0 1 5.6 0" stroke="#fff" stroke-width="1.3" fill="none"/><circle cx="5.5" cy="7" r="1" fill="#fff"/></svg>
    </span>
    <span>4:00 PM</span>
    <span class="status-bar__battery">100% <svg width="17" height="8" viewBox="0 0 17 8"><rect x=".5" y=".5" width="14" height="7" rx="1" stroke="#fff" fill="none"/><rect x="2" y="2" width="11" height="4" fill="#fff"/><rect x="15" y="2.5" width="1.5" height="3" fill="#fff"/></svg></span>
  </div>
  <div class="nav-bar"><span class="nav-btn nav-btn--back">Back</span><span class="nav-btn nav-btn--logout">Log Out</span></div>
  <ul class="product-list">
    <li class="product"><span class="product__thumb"><span role="img" aria-label="Product photo: case of bottles in a wooden crate"></span></span><span class="product__name">WHITE DOILEY 30CM 12INCHES</span><span class="product__price">PRICE <strong>$150.00</strong><span class="product__case">PRICE PER CASE : <em>$25.00</em></span></span><span class="product__actions"><svg width="7" height="9" viewBox="0 0 7 9"><path d="M1 1l4 3.5L1 8" stroke="#888" stroke-width="1.5" fill="none"/></svg><svg width="10" height="10" viewBox="0 0 10 10"><circle cx="5" cy="5" r="5" fill="#3aa62a"/><path d="M5 2.5v5M2.5 5h5" stroke="#fff" stroke-width="1.5"/></svg></span></li>
    <li class="product"><span class="product__thumb"><span role="img" aria-label="Product photo: case of bottles in a wooden crate"></span></span><span class="product__name">WHITE DOILEY 30CM 12INCHES</span><span class="product__price">PRICE <strong>$150.00</strong><span class="product__case">PRICE PER CASE : <em>$25.00</em></span></span><span class="product__actions"><svg width="7" height="9" viewBox="0 0 7 9"><path d="M1 1l4 3.5L1 8" stroke="#888" stroke-width="1.5" fill="none"/></svg><svg width="10" height="10" viewBox="0 0 10 10"><circle cx="5" cy="5" r="5" fill="#3aa62a"/><path d="M5 2.5v5M2.5 5h5" stroke="#fff" stroke-width="1.5"/></svg></span></li>
    <li class="product"><span class="product__thumb"><span role="img" aria-label="Product photo: case of bottles in a wooden crate"></span></span><span class="product__name">WHITE DOILEY 30CM 12INCHES</span><span class="product__price">PRICE <strong>$150.00</strong><span class="product__case">PRICE PER CASE : <em>$25.00</em></span></span><span class="product__actions"><svg width="7" height="9" viewBox="0 0 7 9"><path d="M1 1l4 3.5L1 8" stroke="#888" stroke-width="1.5" fill="none"/></svg><svg width="10" height="10" viewBox="0 0 10 10"><circle cx="5" cy="5" r="5" fill="#3aa62a"/><path d="M5 2.5v5M2.5 5h5" stroke="#fff" stroke-width="1.5"/></svg></span></li>
    <li class="product"><span class="product__thumb"><span role="img" aria-label="Product photo: case of bottles in a wooden crate"></span></span><span class="product__name">WHITE DOILEY 30CM 12INCHES</span><span class="product__price">PRICE <strong>$150.00</strong><span class="product__case">PRICE PER CASE : <em>$25.00</em></span></span><span class="product__actions"><svg width="7" height="9" viewBox="0 0 7 9"><path d="M1 1l4 3.5L1 8" stroke="#888" stroke-width="1.5" fill="none"/></svg><svg width="10" height="10" viewBox="0 0 10 10"><circle cx="5" cy="5" r="5" fill="#3aa62a"/><path d="M5 2.5v5M2.5 5h5" stroke="#fff" stroke-width="1.5"/></svg></span></li>
    <li class="product"><span class="product__thumb"><span role="img" aria-label="Product photo: case of bottles in a wooden crate"></span></span><span class="product__name">WHITE DOILEY 30CM 12INCHES</span><span class="product__price">PRICE <strong>$150.00</strong><span class="product__case">PRICE PER CASE : <em>$25.00</em></span></span><span class="product__actions"><svg width="7" height="9" viewBox="0 0 7 9"><path d="M1 1l4 3.5L1 8" stroke="#888" stroke-width="1.5" fill="none"/></svg><svg width="10" height="10" viewBox="0 0 10 10"><circle cx="5" cy="5" r="5" fill="#3aa62a"/><path d="M5 2.5v5M2.5 5h5" stroke="#fff" stroke-width="1.5"/></svg></span></li>
    <li class="product"><span class="product__thumb"><span role="img" aria-label="Product photo: case of bottles in a wooden crate"></span></span><span class="product__name">WHITE DOILEY 30CM 12INCHES</span><span class="product__price">PRICE <strong>$150.00</strong><span class="product__case">PRICE PER CASE : <em>$25.00</em></span></span><span class="product__actions"><svg width="7" height="9" viewBox="0 0 7 9"><path d="M1 1l4 3.5L1 8" stroke="#888" stroke-width="1.5" fill="none"/></svg><svg width="10" height="10" viewBox="0 0 10 10"><circle cx="5" cy="5" r="5" fill="#3aa62a"/><path d="M5 2.5v5M2.5 5h5" stroke="#fff" stroke-width="1.5"/></svg></span></li>
  </ul>
  <div class="summary"><span class="summary__count">ITEMS IN CART : (9) ITEMS</span><span class="summary__total">TOTAL : $500.00</span></div>
  <div class="search-strip"><span class="search-box"><svg width="6" height="6" viewBox="0 0 6 6"><circle cx="3.5" cy="2.5" r="1.8" stroke="#777" fill="none"/><path d="M2.2 3.8.5 5.5" stroke="#777"/></svg>search</span></div>
</section>

</body>
</html>
```